business card, stationary and envelopes for Insulation Company
Silver Otter Insulation
business card, stationary and envelopes for Insulation Company - Construction
Creative Brief
Bright & Fun-filled
Calvin Rudd
Sales Manager
7W.318 Maple Crest Drive Naperville, Illinois 60563
sales@silverotterinsulation-example.com
www.SilverOtterInsulation-example.com
Services Offered: Attic Insulation Wall Insulation Attic Ventilation Weatherization Attic Decontamination Insulation Removal Types of Insulation Cellulose Fiberglass Spray Foam Blown Batt

```html
<!DOCTYPE html>
<html lang="en">
<head>
<meta charset="utf-8">
<title>Silver Otter Insulation – Stationery Concepts</title>
<link href="https://fonts.googleapis.com/css2?family=Open+Sans:wght@400;700&display=swap" rel="stylesheet">
<style>
:root{
  --bg-top:#6a6a6a;
  --bg-mid:#9a9a9a;
  --bg-low:#5e5e5e;
  --green-dark:#2f6b12;
  --green:#5a9e1e;
  --green-light:#9bd247;
  --paper:#ffffff;
  --ink:#333333;
  --ink-soft:#777777;
  --caption:#e8e8e8;
  --flap-rose:#b9a49a;
  --art-tint:#e9f1dc;
}
*{margin:0;padding:0;box-sizing:border-box}
html,body{width:1200px;height:386px;overflow:hidden}
body{font-family:"Open Sans",Arial,sans-serif;
  background:linear-gradient(180deg,var(--bg-top) 0%,var(--bg-mid) 55%,var(--bg-low) 100%);
  position:relative}
.abs{position:absolute}
.brand{font-weight:700;color:var(--green-dark);display:flex;align-items:center;gap:4px;line-height:1.05}
.brand .mark{width:8px;height:8px;background:var(--green);flex:none}
.brand.on-dark{color:var(--paper)}
.brand.on-dark .mark{background:var(--green-light)}
.caption{font-size:5px;color:var(--caption);text-align:center}

.hero-badge{left:108px;top:10px;width:84px;height:72px;border-radius:8px;
  background:linear-gradient(160deg,var(--green-light),var(--green-dark));
  display:flex;align-items:center;justify-content:center;padding:6px}
.hero-badge .brand{font-size:11px;color:var(--paper);text-align:center}
.sheet-title{left:108px;top:88px;font-size:9px;color:#222}

.card{width:106px;height:64px;box-shadow:0 1px 3px rgba(0,0,0,.45)}
.card.green{background:radial-gradient(circle at 35% 45%,var(--green-light),var(--green-dark) 85%);padding:8px}
.card.white{background:var(--paper);padding:7px}
.card .brand{font-size:8px}
.card .person{font-size:5px;font-weight:700;color:var(--ink)}
.card .role{font-size:4px;color:var(--ink-soft)}
.card .line{font-size:3.4px;color:var(--ink);line-height:1.5}
.card .bar{position:absolute;left:0;right:0;bottom:0;height:6px;background:var(--green)}

.letterhead{width:168px;height:340px;top:8px;background:var(--paper);
  box-shadow:0 1px 4px rgba(0,0,0,.45);padding:10px}
.letterhead .brand{font-size:8px;position:absolute;left:10px;top:10px;width:58px}
.letterhead .brand.centered{left:26px}
.letterhead .contact{position:absolute;right:8px;top:10px;width:72px;font-size:3.2px;color:var(--ink);line-height:1.6;white-space:nowrap}
.letterhead .art{position:absolute;left:30px;top:110px;width:108px;height:180px;border-radius:50% 50% 40% 40%;background:var(--art-tint);opacity:.8}
.letterhead .footer{position:absolute;left:0;right:0;bottom:0;height:8px;background:linear-gradient(90deg,var(--green-dark),var(--green-light))}

.envelope{width:164px;box-shadow:0 1px 3px rgba(0,0,0,.45);background:var(--paper);overflow:hidden}
.envelope .flap{position:absolute;left:0;top:0;width:100%;height:100%}
.envelope .brand{font-size:6px;position:absolute;left:8px;top:6px}
.envelope .bird{position:absolute;left:74px;top:24px;width:14px;height:20px;border-radius:50%;background:var(--green)}
.envelope .addr{position:absolute;left:62px;font-size:3.2px;color:var(--ink)}
</style>
</head>
<body>

<div class="abs hero-badge"><div class="brand">Silver Otter Insulation</div></div>
<div class="abs sheet-title">Stationary Concepts</div>

<div class="abs card green" style="left:8px;top:122px">
  <div class="brand on-dark" style="font-size:10px;width:70px;margin-top:10px"><span class="mark"></span>Silver Otter Insulation</div>
</div>
<div class="abs card white" style="left:120px;top:122px">
  <div class="person">Calvin Rudd</div>
  <div class="role">Sales Manager</div>
  <div class="line" style="margin-top:6px">7W.318 Maple Crest Drive Naperville, Illinois 60563<br>sales@silverotterinsulation-example.com<br>www.SilverOtterInsulation-example.com</div>
  <div class="bar"></div>
</div>
<div class="abs caption" style="left:8px;top:190px;width:106px">Business Card Front</div>
<div class="abs caption" style="left:120px;top:190px;width:106px">Business Card Back</div>

<div class="abs card white" style="left:8px;top:206px">
  <div class="brand" style="font-size:10px;width:70px;margin-top:10px"><span class="mark"></span>Silver Otter Insulation</div>
  <div class="bar"></div>
</div>
<div class="abs card white" style="left:120px;top:206px">
  <div class="person">Calvin Rudd</div>
  <div class="role">Sales Manager</div>
  <div class="line" style="margin-top:6px">7W.318 Maple Crest Drive Naperville, Illinois 60563<br>sales@silverotterinsulation-example.com<br>www.SilverOtterInsulation-example.com</div>
  <div class="bar" style="background:var(--green-dark)"></div>
</div>
<div class="abs caption" style="left:8px;top:274px;width:106px">Business Card Front</div>
<div class="abs caption" style="left:120px;top:274px;width:106px">Business Card Back</div>

<div class="abs letterhead" style="left:246px">
  <div class="brand centered"><span class="mark"></span>Silver Otter Insulation</div>
  <div class="contact">7W.318 Maple Crest Drive<br>Naperville, Illinois 60563<br>sales@silverotterinsulation-example.com<br>www.SilverOtterInsulation-example.com</div>
  <div class="art" role="img" aria-label="Faint mascot illustration watermark"></div>
  <div class="footer"></div>
</div>
<div class="abs caption" style="left:246px;top:354px;width:168px">Letterhead Option 1</div>

<div class="abs letterhead" style="left:442px">
  <div class="brand"><span class="mark"></span>Silver Otter Insulation</div>
  <div class="contact">7W.318 Maple Crest Drive<br>Naperville, Illinois 60563<br>sales@silverotterinsulation-example.com<br>www.SilverOtterInsulation-example.com</div>
  <div class="art" role="img" aria-label="Faint mascot illustration watermark"></div>
  <div class="footer"></div>
</div>
<div class="abs caption" style="left:442px;top:354px;width:168px">Letterhead Option 2</div>

<div class="abs envelope" style="left:628px;top:18px;height:88px">
  <svg class="flap" viewBox="0 0 164 88" preserveAspectRatio="none" aria-hidden="true">
    <defs><linearGradient id="envGreen" x1="0" y1="0" x2="0" y2="1"><stop offset="0" stop-color="#9bd247"/><stop offset="1" stop-color="#2f6b12"/></linearGradient></defs>
    <rect width="164" height="88" fill="url(#envGreen)"/>
    <polygon points="0,0 164,0 82,50" fill="#ffffff" opacity=".15"/>
  </svg>
  <div class="brand on-dark"><span class="mark"></span>Silver Otter Insulation</div>
</div>
<div class="abs caption" style="left:628px;top:108px;width:164px">Envelope Option 1</div>

<div class="abs envelope" style="left:628px;top:122px;height:70px">
  <svg class="flap" viewBox="0 0 164 70" preserveAspectRatio="none" aria-hidden="true">
    <polygon points="0,0 164,0 82,34" fill="#b9a49a"/>
  </svg>
  <div class="bird" role="img" aria-label="Small mascot illustration"></div>
  <div class="addr" style="top:52px">www.SilverOtterInsulation-example.com</div>
</div>

<div class="abs envelope" style="left:636px;top:204px;height:48px">
  <svg class="flap" viewBox="0 0 164 48" preserveAspectRatio="none" aria-hidden="true">
    <polyline points="0,0 82,22 164,0" fill="none" stroke="#cccccc" stroke-width="1"/>
  </svg>
  <div class="brand"><span class="mark"></span>Silver Otter Insulation</div>
</div>

<div class="abs envelope" style="left:628px;top:238px;height:46px">
  <div class="brand"><span class="mark"></span>Silver Otter Insulation</div>
  <div class="addr" style="top:30px">7W.318 Maple Crest Drive Naperville, Illinois 60563</div>
  <div style="position:absolute;left:0;right:0;bottom:0;height:4px;background:var(--green)"></div>
</div>
<div class="abs caption" style="left:628px;top:288px;width:164px">Envelope Option 2</div>

</body>
</html>
```